Kavak Verbatics web design: a translation company with corporate clients

Need a new website for my translation and localization company with file uploading capacity directed to email for quotation

old (very old) web site is www.kvkaktarim.example you can use the content text there or lorem ipsum, We will provide the texts. It will be in English - Turkish - French and German
For the content and overall layout: https://www.pellardlanguages.example/

For the color scheme you'll need to see logo's colors.

I am rebranding so new logo is uploaded The new adress will be www.kavakverbatics.example

Target Market(s)

Primarily corporate clients

Industry/Entity Type

It Company

Coding

Coded - Design and coding required

Number of Pages Required

5+ page

Font styles to use
Other font styles liked:
• Calibri

Requirements
Must have
• References on homepage (logos will be sent during design phase)
• Services: Translation, Interpretation, Localization&Consultancy, Translation API
• Quotation Form and file uploading
• Simple layout evoking reliability, speed and accuracy
Nice to have
• For the content and overall layout: https://www.pellardlanguages.example/
• Separate page for Translation Services: Marketing Translation, Legal Translation, Technical Translation, Personal Translation
• and texts under these headings
Should not have
• Old style
• Complex design

```html
<!DOCTYPE html>
<html lang="en">
<head>
<meta charset="utf-8">
<title>Kavak Verbatics – Translation, Localization &amp; Consultancy</title>
<link rel="stylesheet" href="https://fonts.googleapis.com/css2?family=Lato:wght@300;400;700;900&display=swap">
<style>
:root{
  --green:#5b7a2e;
  --green-dark:#3f5f25;
  --green-light:#6e8f3c;
  --orange:#f39a1e;
  --ink:#333333;
  --muted:#666666;
  --tile:#ececec;
  --line:#d6d6d6;
  --footer:#333333;
  --footer-bottom:#222222;
  --white:#ffffff;
}
*{box-sizing:border-box;margin:0;padding:0}
html,body{width:1200px;height:2995px;overflow:hidden;background:var(--white)}
body{font-family:'Lato',sans-serif;color:var(--ink)}
.page{position:relative;width:1200px;height:2995px;overflow:hidden}
.abs{position:absolute}

/* top bar */
.topbar{left:0;top:0;width:1200px;height:40px;background:#111}
.topbar-social{right:128px;top:6px;display:flex;gap:8px}
.topbar-social span{width:26px;height:26px;border-radius:50%;background:#5d5d5d;display:block}
.lang-switch{right:0;top:0;width:102px;height:40px;background:#4a4a4a;color:#fff;font-size:13px;font-weight:700;display:flex;align-items:center;justify-content:center;gap:6px}
.lang-switch i{width:14px;height:10px;background:#c9c9c9;display:block}

/* header */
.header{left:0;top:40px;width:1200px;height:108px;background:#fff;border-bottom:1px solid #e2e2e2}
.brand{left:80px;top:22px}
.brand-name{font-size:34px;font-weight:400;color:var(--green);line-height:1;letter-spacing:1px}
.brand-tag{margin-top:10px;font-size:10px;font-weight:700;color:var(--green);letter-spacing:.3px}
.nav{left:400px;top:46px;display:flex;gap:22px;font-size:14px;font-weight:900;letter-spacing:.4px}
.nav a{color:#222;text-decoration:none}
.nav a.active{color:var(--orange)}

/* hero */
.hero{left:0;top:148px;width:1200px;height:546px;background:radial-gradient(ellipse at 35% 45%,#3f7a4a 0%,#2f6238 55%,#244f2c 100%)}
.hero-badge{left:778px;top:212px;width:380px;height:380px;border-radius:50%;background:#5c8a45;display:flex;flex-direction:column;align-items:center;justify-content:center;text-align:center;font-weight:900;font-size:37px;line-height:52px;color:#fff;letter-spacing:.5px}
.hero-badge em{font-style:normal;color:var(--orange)}
.hero-dots{left:926px;top:618px;display:flex;gap:8px}
.hero-dots span{width:16px;height:16px;border-radius:50%;background:#bbb;border:2px solid #fff}
.hero-dots span.on{background:var(--orange)}

/* section titles */
.section-title{left:0;width:1200px;text-align:center;font-size:34px;font-weight:300;letter-spacing:1px;color:#444}
.section-title b{font-weight:300;color:var(--green)}
.title-rule{left:245px;width:710px;height:2px;background:var(--line)}
.title-rule::before,.title-rule::after{content:"";position:absolute;top:-2px;height:4px;width:52px}
.title-rule::before{left:300px;background:var(--orange)}
.title-rule::after{left:356px;background:var(--green)}

/* offers */
.offers{left:0;top:850px;width:1200px;height:232px;background:var(--tile)}
.offer{top:0;width:300px;height:232px;text-align:center}
.offer .icon{position:absolute;left:100px;top:28px;width:100px;height:100px}
.offer .label{position:absolute;left:0;width:300px;top:174px;font-size:21px;font-weight:700;color:#222;line-height:26px}
.offer.featured{background:var(--orange)}
.offer.featured .label{color:#fff}
.knob{width:48px;height:48px;border-radius:50%;position:absolute}
.offer-copy{left:100px;top:1118px;width:1000px;text-align:center;font-size:13px;line-height:25px;color:#444}
.more-link{left:0;top:1236px;width:1200px;text-align:center;font-size:12px;color:var(--orange);font-weight:700;letter-spacing:.3px}

/* clients */
.clients-band{left:0;top:1310px;width:1200px;height:352px;background:#f7f7f7;border-top:1px solid #e4e4e4}
.clients-strip{left:40px;top:1476px;width:1120px;height:124px;background:#fff;border-radius:4px}
.client{top:1502px;width:196px;height:72px;border:1px solid #dcdcdc;background:#fff;display:flex;align-items:center;justify-content:center;gap:8px;font-size:19px;font-weight:700;color:var(--green-dark)}
.client i{width:14px;height:14px;background:var(--green-dark);display:block}
.carousel-arrow{top:1520px;width:20px;height:36px}

/* quote form */
.quote{left:0;top:1662px;width:1200px;height:560px;background:linear-gradient(120deg,#5a7a2d 0%,#617f33 60%,#6a8a3a 100%)}
.quote-title{left:0;top:1714px;width:1200px;text-align:center;color:#fff;font-size:34px;font-weight:300;letter-spacing:1px}
.quote-sub{left:0;top:1766px;width:1200px;text-align:center;color:#c7d8a6;font-size:19px;font-style:italic;font-weight:300}
.steps-line{left:80px;top:1844px;width:1040px;height:3px;background:#fff}
.steps-line .done{position:absolute;left:0;top:0;width:348px;height:3px;background:var(--orange)}
.step-dot{top:1834px;width:22px;height:22px;border-radius:50%;background:#fff;border:3px solid #e0e0e0}
.step-dot.on{background:var(--orange);border-color:#f8c47a}
.step-label{top:1862px;width:240px;text-align:center;font-size:14px;font-weight:900;color:#fff;letter-spacing:.3px}
.step-label.on{color:var(--orange)}
.field-label{font-size:14px;font-weight:700;color:#fff}
.select{height:36px;background:#fff;border-radius:3px;font-size:12px;color:#555;display:flex;align-items:center;padding-left:12px}
.select svg{position:absolute;right:10px;top:13px}
.listbox{left:82px;top:2040px;width:400px;height:116px;background:#fff;border-radius:3px;padding:10px 12px;font-size:13px;line-height:19px;color:#555}
.swap-arrows{left:486px;top:2082px;color:#ddd;font-size:14px}
.target-box{left:516px;top:2040px;width:400px;height:116px;background:#fff;border-radius:3px}
.next-btn{left:942px;top:2040px;width:178px;height:54px;background:var(--orange);color:#fff;font-size:21px;font-weight:900;display:flex;align-items:center;justify-content:center;border-radius:2px;letter-spacing:.5px}

/* translation services */
.service{top:2398px;width:160px;text-align:center}
.service svg{display:block;margin:0 auto}
.service .label{margin-top:20px;font-size:17px;font-weight:900;line-height:24px;color:#222;letter-spacing:.3px}

/* footer */
.footer{left:0;top:2650px;width:1200px;height:294px;background:var(--footer);border-top:4px solid var(--green)}
.foot-head{top:2694px;font-size:16px;font-weight:900;color:#fff;letter-spacing:.5px}
.foot-head::after{content:"";display:block;width:58px;height:2px;background:var(--orange);margin-top:10px}
.foot-rule{top:2728px;height:1px;background:#4c4c4c}
.quick-links{left:82px;top:2744px;list-style:none;font-size:13px;line-height:25.5px;color:#ddd}
.quick-links li::before{content:"› ";color:#999}
.contact{left:294px;top:2748px;width:250px;font-size:13px;color:#ddd;line-height:19px}
.contact-row{display:flex;gap:10px;margin-bottom:22px}
.contact-row svg{flex:none;margin-top:2px}
.map{left:588px;top:2748px;width:260px;height:144px;background:linear-gradient(135deg,#c9d7e3,#e8e4d6 55%,#bcd0b4)}
.social{left:916px;top:2752px;list-style:none;font-size:14px;color:#ddd}
.social li{display:flex;align-items:center;gap:14px;height:40px;letter-spacing:.5px}
.social li span{width:26px;height:26px;border-radius:50%;background:#5d5d5d}
.copyright{left:0;top:2944px;width:1200px;height:51px;background:var(--footer-bottom);color:#ddd;font-size:13px;display:flex;align-items:center;justify-content:center}
</style>
</head>
<body>
<div class="page">

  <!-- top bar -->
  <div class="abs topbar"></div>
  <div class="abs topbar-social"><span></span><span></span><span></span><span></span></div>
  <div class="abs lang-switch"><i></i>English <svg width="10" height="7" viewBox="0 0 10 7"><path d="M1 1l4 4 4-4" stroke="#fff" stroke-width="1.6" fill="none"/></svg></div>

  <!-- header -->
  <header class="abs header"></header>
  <div class="abs brand">
    <div class="brand-name">KAVAK<br>VERBATICS</div>
    <div class="brand-tag">TRANSLATION, LOCALIZATION &amp; CONSULTANCY</div>
  </div>
  <nav class="abs nav">
    <a class="active" href="#">HOME</a><a href="#">SERVICES</a><a href="#">LANGUAGES</a><a href="#">RESOURCES</a><a href="#">PRICING</a><a href="#">ABOUT US</a><a href="#">BLOG</a><a href="#">CONTACT US</a>
  </nav>

  <!-- hero -->
  <section class="abs hero" role="img" aria-label="Chalkboard with greetings written in many languages, arranged as a speech bubble"></section>
  <div class="abs hero-badge">DELIVERY ON<br>TIME WITH<br><em>PERFECT QUALITY</em></div>
  <div class="abs hero-dots"><span></span><span class="on"></span><span></span><span></span></div>

  <!-- what we offer -->
  <h2 class="abs section-title" style="top:732px">WHAT WE <b>OFFER</b></h2>
  <div class="abs title-rule" style="top:800px"></div>

  <div class="abs offers">
    <div class="abs offer" style="left:0">
      <svg class="icon" viewBox="0 0 100 100"><circle cx="60" cy="58" r="34" fill="#dcdcdc"/><rect x="44" y="42" width="22" height="22" rx="3" fill="#333"/><rect x="58" y="54" width="22" height="22" rx="3" fill="#555" stroke="#dcdcdc" stroke-width="2"/><text x="55" y="58" font-family="Lato,sans-serif" font-size="13" font-weight="900" fill="#fff" text-anchor="middle">文</text><text x="69" y="71" font-family="Lato,sans-serif" font-size="13" font-weight="900" fill="#fff" text-anchor="middle">A</text></svg>
      <div class="label">TRANSLATION</div>
    </div>
    <div class="abs offer featured" style="left:300px">
      <svg class="icon" viewBox="0 0 100 100"><circle cx="50" cy="60" r="30" fill="#fbb451"/><circle cx="50" cy="60" r="24" fill="none" stroke="#fff" stroke-width="2"/><path d="M37 52h20v12h-12l-6 5v-5h-2z" fill="#fff"/><path d="M50 60h14v10h-2v4l-5-4h-7z" fill="#fff" stroke="#fbb451" stroke-width="1.5"/></svg>
      <div class="label">INTERPRETATION</div>
    </div>
    <div class="abs offer" style="left:600px">
      <svg class="icon" viewBox="0 0 100 100"><circle cx="60" cy="58" r="34" fill="#dcdcdc"/><path d="M38 56l12-8 10 4 10-4 12 8-14 12h-6z" fill="#333"/></svg>
      <div class="label">LOCALIZATION &amp;<br>CONSULTANCY</div>
    </div>
    <div class="abs offer" style="left:900px">
      <svg class="icon" viewBox="0 0 100 100"><circle cx="60" cy="58" r="34" fill="#dcdcdc"/><circle cx="64" cy="54" r="11" fill="none" stroke="#333" stroke-width="6" stroke-dasharray="4 3"/><circle cx="48" cy="70" r="7" fill="none" stroke="#333" stroke-width="4" stroke-dasharray="3 2"/></svg>
      <div class="label">TRANSLATION API</div>
    </div>
    <div class="knob" style="left:276px;top:92px;background:var(--orange)"></div>
    <div class="knob" style="left:576px;top:92px;background:var(--orange)"></div>
    <div class="knob" style="left:876px;top:92px;background:var(--tile)"></div>
  </div>

  <p class="abs offer-copy">Lorem ipsum dolor sit amet, consectetuer adipiscing elit, sed diam nonummy nibh euismod tincidunt ut laoreet dolore magna aliquam erat volutpat. Ut wisi enim ad minim veniam, quis nostrud exerci tation ullamcorper suscipit lobortis nisl ut aliquip ex ea commodo consequat. Duis autem vel eum iriure dolor in hendrerit in vulputate velit esse molestie consequat, vel illum dolore eu feugiat nulla facilisis at vero eros et accumsan et iusto odio dignissim qui blandit praesent luptatum zzril delenit augue duis dolore te feugait nulla facilisi ullamcorper suscipit lobortis nisl ut aliquip ex ea commodo consequa.</p>
  <div class="abs more-link">KNOW MORE ABOUT SERVICES »</div>

  <!-- clients -->
  <div class="abs clients-band"></div>
  <h2 class="abs section-title" style="top:1362px">OUR <b>CLIENTS</b></h2>
  <div class="abs title-rule" style="top:1430px"></div>
  <div class="abs clients-strip"></div>
  <svg class="abs carousel-arrow" style="left:80px" viewBox="0 0 20 36"><path d="M16 2L4 18l12 16" stroke="#777" stroke-width="2" fill="none"/></svg>
  <svg class="abs carousel-arrow" style="left:1104px" viewBox="0 0 20 36"><path d="M4 2l12 16L4 34" stroke="#777" stroke-width="2" fill="none"/></svg>
  <div class="abs client" style="left:130px"><i></i>Voltara</div>
  <div class="abs client" style="left:380px"><i></i>Kestrel Yatırım</div>
  <div class="abs client" style="left:630px"><i></i>Norvale University</div>
  <div class="abs client" style="left:884px;font-size:17px"><i></i>Tamsin Orland Vey</div>

  <!-- quote form -->
  <section class="abs quote"></section>
  <h2 class="abs quote-title">TRANSLATION QUOTE FORM</h2>
  <div class="abs quote-sub">Quick &amp; Easy In Just 3 Steps</div>
  <div class="abs steps-line"><div class="done"></div></div>
  <div class="abs step-dot on" style="left:228px"></div>
  <div class="abs step-dot" style="left:588px"></div>
  <div class="abs step-dot" style="left:922px"></div>
  <div class="abs step-label on" style="left:120px">TIME &amp; LANGUAGES</div>
  <div class="abs step-label" style="left:480px">UPLOAD FILES</div>
  <div class="abs step-label" style="left:814px">YOUR INFO</div>

  <div class="abs field-label" style="left:82px;top:1918px">Time Frame</div>
  <div class="abs field-label" style="left:434px;top:1918px">Certification</div>
  <div class="abs field-label" style="left:786px;top:1918px">Translate From</div>
  <div class="abs select" style="left:82px;top:1950px;width:332px">Express (Within 48 hrs)<svg width="12" height="8" viewBox="0 0 12 8"><path d="M1 1l5 5 5-5" stroke="#333" stroke-width="1.8" fill="none"/></svg></div>
  <div class="abs select" style="left:434px;top:1950px;width:332px">Not Required<svg width="12" height="8" viewBox="0 0 12 8"><path d="M1 1l5 5 5-5" stroke="#333" stroke-width="1.8" fill="none"/></svg></div>
  <div class="abs select" style="left:786px;top:1950px;width:334px">English<svg width="12" height="8" viewBox="0 0 12 8"><path d="M1 1l5 5 5-5" stroke="#333" stroke-width="1.8" fill="none"/></svg></div>

  <div class="abs field-label" style="left:82px;top:2010px">Translate To</div>
  <div class="abs listbox">Arabic<br>Chinese Simplified<br>Chinese Traditional<br>English<br>English(USA)</div>
  <div class="abs swap-arrows">⇄</div>
  <div class="abs target-box"></div>
  <div class="abs next-btn">NEXT STEP »</div>

  <!-- translation services -->
  <h2 class="abs section-title" style="top:2268px">OUR <b>TRANSLATION</b> SERVICES</h2>
  <div class="abs title-rule" style="top:2334px"></div>

  <div class="abs service" style="left:116px">
    <svg width="130" height="130" viewBox="0 0 130 130"><circle cx="65" cy="65" r="62" fill="none" stroke="var(--orange)" stroke-width="3" stroke-dasharray="1 7" stroke-linecap="round"/><circle cx="65" cy="65" r="48" fill="#e6e6e6"/><rect x="52" y="42" width="24" height="44" rx="4" fill="#333"/><rect x="56" y="48" width="16" height="30" fill="#e6e6e6"/><path d="M62 56l10-6v22l-10-6z" fill="var(--orange)"/></svg>
    <div class="label">MARKETING<br>TRANSLATION</div>
  </div>
  <div class="abs service" style="left:320px">
    <svg width="130" height="130" viewBox="0 0 130 130"><circle cx="65" cy="65" r="62" fill="none" stroke="var(--orange)" stroke-width="3" stroke-dasharray="1 7" stroke-linecap="round"/><circle cx="65" cy="65" r="48" fill="#e6e6e6"/><rect x="52" y="40" width="28" height="14" rx="2" transform="rotate(-40 66 47)" fill="#333"/><rect x="62" y="52" width="6" height="30" transform="rotate(-40 65 67)" fill="#333"/><rect x="44" y="84" width="30" height="6" fill="#333"/></svg>
    <div class="label">LEGAL<br>TRANSLATION</div>
  </div>
  <div class="abs service" style="left:522px">
    <svg width="130" height="130" viewBox="0 0 130 130"><circle cx="65" cy="65" r="62" fill="none" stroke="var(--orange)" stroke-width="3" stroke-dasharray="1 7" stroke-linecap="round"/><circle cx="65" cy="65" r="48" fill="#e6e6e6"/><path d="M46 84l34-34" stroke="#333" stroke-width="7" stroke-linecap="round"/><path d="M48 48l34 34" stroke="#333" stroke-width="7" stroke-linecap="round"/><circle cx="82" cy="48" r="7" fill="none" stroke="#333" stroke-width="4"/></svg>
    <div class="label">TECHNICAL<br>TRANSLATION</div>
  </div>
  <div class="abs service" style="left:724px">
    <svg width="130" height="130" viewBox="0 0 130 130"><circle cx="65" cy="65" r="62" fill="none" stroke="var(--orange)" stroke-width="3" stroke-dasharray="1 7" stroke-linecap="round"/><circle cx="65" cy="65" r="48" fill="#e6e6e6"/><rect x="44" y="70" width="8" height="14" fill="#333"/><rect x="56" y="62" width="8" height="22" fill="#333"/><rect x="68" y="56" width="8" height="28" fill="#333"/><rect x="80" y="66" width="8" height="18" fill="#333"/><text x="66" y="52" font-family="Lato,sans-serif" font-size="18" font-weight="900" fill="#333" text-anchor="middle">$</text></svg>
    <div class="label">FINANCIAL<br>TRANSLATION</div>
  </div>
  <div class="abs service" style="left:926px">
    <svg width="130" height="130" viewBox="0 0 130 130"><circle cx="65" cy="65" r="62" fill="none" stroke="var(--orange)" stroke-width="3" stroke-dasharray="1 7" stroke-linecap="round"/><circle cx="65" cy="65" r="48" fill="#e6e6e6"/><rect x="48" y="42" width="34" height="44" rx="3" fill="#333"/><rect x="54" y="52" width="22" height="3" fill="#e6e6e6"/><rect x="54" y="60" width="22" height="3" fill="#e6e6e6"/><rect x="54" y="68" width="14" height="3" fill="#e6e6e6"/></svg>
    <div class="label">PERSONAL<br>TRANSLATION</div>
  </div>

  <!-- footer -->
  <footer class="abs footer"></footer>
  <div class="abs foot-head" style="left:82px">QUICK LINKS</div>
  <div class="abs foot-head" style="left:294px">CONTACT US</div>
  <div class="abs foot-head" style="left:584px">LOCATE US</div>
  <div class="abs foot-head" style="left:916px">SOCIAL MEDIA</div>
  <div class="abs foot-rule" style="left:140px;width:114px"></div>
  <div class="abs foot-rule" style="left:352px;width:176px"></div>
  <div class="abs foot-rule" style="left:642px;width:210px"></div>
  <div class="abs foot-rule" style="left:974px;width:146px"></div>

  <ul class="abs quick-links">
    <li>Home</li><li>About Us</li><li>Services</li><li>Online Translation</li><li>Graphic Design</li><li>Contact Us</li>
  </ul>

  <div class="abs contact">
    <div class="contact-row"><svg width="12" height="16" viewBox="0 0 12 16"><path d="M6 0a6 6 0 0 1 6 6c0 4-6 10-6 10S0 10 0 6a6 6 0 0 1 6-6z" fill="#ccc"/><circle cx="6" cy="6" r="2.2" fill="#333"/></svg><div><b>Kavak Verbatics,</b><br>Lorem ipsum dolor sit amet,<br>consectetuer adipiscing elit</div></div>
    <div class="contact-row" style="font-size:15px;font-weight:700"><svg width="14" height="14" viewBox="0 0 14 14"><path d="M3 0l3 3-2 2c1 2 3 4 5 5l2-2 3 3-2 3C6 14 0 8 0 3z" fill="#ccc"/></svg>123-456-7890</div>
    <div class="contact-row"><svg width="14" height="10" viewBox="0 0 14 10"><rect width="14" height="10" fill="#ccc"/><path d="M0 0l7 6 7-6" stroke="#333" stroke-width="1.2" fill="none"/></svg>info@kavakverbatics.example</div>
  </div>

  <div class="abs map" role="img" aria-label="Street map showing the office location"></div>

  <ul class="abs social">
    <li><span></span>FRIENDWALL</li>
    <li><span></span>CHIRPLINE</li>
    <li><span></span>WORKRING</li>
    <li><span></span>CIRCLECAST</li>
  </ul>

  <div class="abs copyright">Copyright © 2016&nbsp;<b>Kavak Verbatics</b>&nbsp;|&nbsp;All Rights Reserved.</div>
</div>
</body>
</html>
```